Consulting firm needs a professional letterhead design

We need a professional letterhead design which is simple but unique. It should carry attributes of the latest designs in the market suitable for professional environmental consultancies.

- The logo is attached for you to USE.
- Our preferred color scheme is that shown in the logo.
- Letterhead text color is your choice to make.
- Logo to the left and text to the right plus slogan/tagline is desirable for this letterhead.

Use any address etc. of your choice in the letterhead.

Target Market(s)

Consulting firms and government agencies

Industry/Entity Type

Environmental Consultant

Colors
acd037
fece3e
85cae6
3277b5

Requirements
Must have
• Logo supplied and color scheme must be used.
Nice to have
• Nexa font is used in the Logo, so it would ne nice to have nexa font in the letterhead too.

```html
<!DOCTYPE html>
<html lang="en">
<head>
<meta charset="utf-8">
<title>Verdantis Letterhead</title>
<link href="https://fonts.googleapis.com/css2?family=Poppins:wght@500;600;700&display=swap" rel="stylesheet">
<style>
  :root {
    --paper: #ffffff;
    --ink: #3a3e55;
    --ink-soft: #2b2d3a;
    --green: #2fae4e;
    --orange: #f39323;
    --brand-green: #acd037;
  }
  * { box-sizing: border-box; margin: 0; padding: 0; }
  html, body {
    width: 927px;
    height: 1200px;
    overflow: hidden;
    background: var(--paper);
  }
  .letterhead {
    position: relative;
    width: 927px;
    height: 1200px;
    background: var(--paper);
    font-family: "Poppins", sans-serif;
    color: var(--ink-soft);
  }
  .brand {
    position: absolute;
    left: 91px;
    top: 78px;
    display: flex;
    align-items: center;
    gap: 12px;
  }
  .brand-mark {
    width: 40px;
    height: 40px;
    background: var(--brand-green);
  }
  .brand-name {
    font-size: 30px;
    font-weight: 700;
    letter-spacing: 1px;
    line-height: 1;
    color: var(--ink);
  }
  .brand-tagline {
    font-size: 12px;
    font-weight: 600;
    line-height: 1.2;
    color: var(--ink);
    margin-top: 2px;
  }
  .contact {
    position: absolute;
    right: 91px;
    top: 966px;
    display: flex;
    flex-direction: column;
    gap: 14px;
  }
  .contact-row {
    display: flex;
    align-items: center;
    justify-content: flex-end;
    gap: 20px;
    height: 42px;
  }
  .contact-text {
    text-align: right;
    font-size: 11.5px;
    font-weight: 600;
    line-height: 1.6;
    color: var(--ink-soft);
  }
  .contact-icon {
    width: 42px;
    height: 42px;
    display: flex;
    align-items: center;
    justify-content: center;
  }
  .contact-icon.is-green { background: var(--green); }
  .contact-icon.is-orange { background: var(--orange); }
  .contact-icon svg { width: 22px; height: 22px; }
</style>
</head>
<body>
  <main class="letterhead">
    <header class="brand">
      <div class="brand-mark"></div>
      <div class="brand-text">
        <div class="brand-name">VERDANTIS</div>
        <div class="brand-tagline">Turning research into sound policy</div>
      </div>
    </header>

    <footer class="contact">
      <div class="contact-row">
        <p class="contact-text">555 014 2368</p>
        <span class="contact-icon is-green">
          <svg viewBox="0 0 24 24" aria-hidden="true">
            <path d="M6.6 10.8a15.1 15.1 0 0 0 6.6 6.6l2.2-2.2c.3-.3.7-.4 1-.2 1.1.4 2.3.6 3.6.6.6 0 1 .4 1 1V20c0 .6-.4 1-1 1A17 17 0 0 1 3 4c0-.6.4-1 1-1h3.5c.6 0 1 .4 1 1 0 1.3.2 2.5.6 3.6.1.3 0 .7-.2 1z" fill="#fff"/>
          </svg>
        </span>
      </div>
      <div class="contact-row">
        <p class="contact-text">info@verdantis.com<br>www.verdantis.com</p>
        <span class="contact-icon is-orange">
          <svg viewBox="0 0 24 24" aria-hidden="true">
            <rect x="3" y="6" width="18" height="12" rx="1" fill="#fff"/>
            <path d="M3.5 6.5 12 13l8.5-6.5" fill="none" stroke="#f39323" stroke-width="1.6"/>
          </svg>
        </span>
      </div>
      <div class="contact-row">
        <p class="contact-text">Harbor Lane 48,<br>Suite 210, NY10031</p>
        <span class="contact-icon is-green">
          <svg viewBox="0 0 24 24" aria-hidden="true">
            <path d="M12 2a7 7 0 0 0-7 7c0 5.2 7 13 7 13s7-7.8 7-13a7 7 0 0 0-7-7z" fill="#fff"/>
            <circle cx="12" cy="9" r="2.6" fill="#2fae4e"/>
          </svg>
        </span>
      </div>
    </footer>
  </main>
</body>
</html>
```